3 fold Flyer Design (A4)

We are offering a good value, professional, Search Engine Optimisation package which is being offered with a 'free' entry onto a local web site. and need to advertise the benefits within a 3 fold flyer. The content may change to show the name of a differen local website (e.g. www.harrowmeadlive.com . The design must look exciting, this is a great offer!

We have attached a draft of the content to the brief. A new brief has been atached 05/01/2011
Updates

Reason: Having viewed the existing designs we feel a need for change to a more dynamic 'sales' approach

Having reviewd the designs we decided to change our approah to make the brochure more sales led than professional.
To compensate for this we have increased the budget a little.
We have also added new text and improved the brief.
Thanks

Target Market(s)

business owners in the North West. Mostly private businesses from shops to manufacturing. Mostly in competitive markets.

Industry/Entity Type

It Professional

Requirements
Must have
• Bright fresh approach which gets over the benefit of increasing business. Happy and positive, with the concept of success.

The Rupert vane Internet logo added to the back page small in size. (attached)
Nice to have
• design which gives the reader confidence to buy
Should not have
• Boring pictures

```html
<!DOCTYPE html>
<html lang="en">
<head>
<meta charset="utf-8">
<title>Rupert vane Internet Solutions – Trifold Flyer</title>
<link rel="stylesheet" href="https://fonts.googleapis.com/css2?family=Source+Sans+3:wght@400;600;700&family=Open+Sans:wght@600;700&display=swap">
<style>
  :root {
    --teal-deep: #1f7a80;
    --teal-mid: #3f9aa0;
    --teal-light: #8fd3da;
    --aqua-pale: #c8eef2;
    --aqua-bright: #5fd0dc;
    --grey-text: #6b6b6b;
    --white: #ffffff;
    --ink-teal: #1a7f8a;
  }
  * { box-sizing: border-box; margin: 0; padding: 0; }
  html, body { width: 1200px; height: 927px; overflow: hidden; background: var(--white); }
  .flyer {
    position: relative; width: 1200px; height: 927px; overflow: hidden;
    font-family: "Source Sans 3", "Myriad Pro", sans-serif;
    background: var(--white);
  }
  .sky-streaks {
    position: absolute; top: 0; right: 0; width: 760px; height: 110px;
    background: linear-gradient(100deg, rgba(255,255,255,0) 0%, var(--aqua-pale) 45%, var(--teal-light) 80%, var(--aqua-bright) 100%);
    opacity: .75;
  }
  .sky-block { position: absolute; background: var(--aqua-pale); opacity: .8; }
  .teal-band {
    position: absolute; left: 0; top: 429px; width: 1200px; height: 498px;
    background: linear-gradient(180deg, var(--teal-mid) 0%, #5aa9ad 40%, #4a9fa5 70%, var(--teal-deep) 100%);
  }
  .band-stripe { position: absolute; left: 0; width: 840px; height: 12px; background: rgba(31,110,116,.55); }
  .cross-v { position: absolute; left: 44px; top: 368px; width: 20px; height: 306px; background: rgba(143,211,218,.35); }
  .cross-h { position: absolute; left: 0; top: 452px; width: 132px; height: 8px; background: rgba(143,211,218,.45); }
  .left-glow { position: absolute; left: 0; top: 368px; width: 115px; height: 61px; background: var(--aqua-pale); opacity: .8; }

  .value-panel { position: absolute; left: 42px; top: 112px; width: 330px; color: var(--grey-text); }
  .value-panel h2 { font-size: 29px; font-weight: 600; margin-bottom: 20px; }
  .value-panel p { font-size: 15.6px; line-height: 1.05; margin-bottom: 20px; }
  .value-panel .contact { color: var(--ink-teal); }

  .photo { position: absolute; }
  .photo-strategist {
    left: 390px; top: 200px; width: 417px; height: 228px;
    background: linear-gradient(90deg, #ffffff 0%, #f1f1ef 45%, #d9cfc6 70%, #f4f4f4 100%);
  }
  .photo-presenter {
    left: 839px; top: 374px; width: 337px; height: 446px;
    background: linear-gradient(160deg, #f4f6f6 0%, #e4e8ea 40%, #c9cfd3 70%, #eef0f0 100%);
  }

  .promo-intro { position: absolute; left: 45px; top: 475px; width: 345px; color: var(--white); }
  .promo-intro h3 { font-size: 13px; font-weight: 400; color: var(--aqua-pale); line-height: 1.05; margin-bottom: 6px; }
  .promo-intro p { font-size: 9.6px; line-height: 1.15; }

  .traffic-note {
    position: absolute; left: 430px; top: 462px; width: 340px; text-align: center;
    font-family: "Open Sans", sans-serif; font-weight: 600; color: var(--white);
    font-size: 13px; letter-spacing: .06em; line-height: 1.2;
  }
  .traffic-note .guarantee { display: block; margin-top: 14px; color: var(--aqua-pale); }

  .headline {
    position: absolute; left: 838px; top: 44px; color: var(--grey-text);
    font-size: 40px; font-weight: 700; line-height: .9; letter-spacing: -.005em;
  }
  .headline .accent { color: var(--ink-teal); }

  .offer-strip { position: absolute; left: 829px; top: 300px; width: 358px; height: 63px; background: var(--aqua-bright); opacity: .55; }
  .offer-strip-top { position: absolute; left: 1000px; top: 288px; width: 180px; height: 40px; background: var(--aqua-pale); opacity: .8; }
  .offer-badge { position: absolute; left: 820px; top: 200px; width: 172px; height: 172px; }
  .bogof {
    position: absolute; left: 998px; top: 244px; color: var(--grey-text);
    font-size: 29px; font-weight: 600; line-height: .9;
  }
  .deal-caption {
    position: absolute; left: 838px; top: 833px; width: 350px; color: var(--white);
    font-size: 17.5px; line-height: 1.05;
  }
</style>
</head>
<body>
<div class="flyer">
  <div class="sky-streaks"></div>
  <div class="sky-block" style="left:374px;top:26px;width:66px;height:20px;"></div>
  <div class="sky-block" style="left:620px;top:0;width:40px;height:8px;"></div>
  <div class="sky-block" style="left:940px;top:18px;width:30px;height:12px;"></div>

  <div class="teal-band">
    <div class="band-stripe" style="top:288px;"></div>
    <div class="band-stripe" style="top:302px;height:4px;opacity:.6;"></div>
  </div>
  <div class="left-glow"></div>
  <div class="cross-v"></div>
  <div class="cross-h"></div>

  <section class="value-panel">
    <h2>Great Value for Money</h2>
    <p>We are offering all of the above for only £180 per month, subject to a 12 month contract, making this one of the most cost effective Internet Marketing packages in the UK.</p>
    <p>For more information please call</p>
    <p>Rupert vane Internet Solutions on</p>
    <p class="contact">08000 47 19 63<br>or email info@rupertvane.net.</p>
  </section>

  <div class="photo photo-strategist" role="img" aria-label="Photo of a businessman drawing a growth curve with a marker"></div>

  <section class="promo-intro">
    <h3>Attract more new customers by promoting your website in two great ways</h3>
    <p>Take advantage of our cost effective Internet Marketing package where you will receive coverage across your local ‘Onlines’ directories as well as a professional Search Engine Optimisation package.</p>
  </section>

  <p class="traffic-note">Please note that<br>increased traffic to your website is<br>normally experienced after month three.<span class="guarantee">Guarentee?</span></p>

  <h1 class="headline">Would you like<br>to attract more<br><span class="accent">customers</span><br>to your business?</h1>

  <div class="offer-strip-top"></div>
  <div class="offer-strip"></div>
  <svg class="offer-badge" viewBox="0 0 172 172" aria-label="Special offer for 2011">
    <circle cx="86" cy="86" r="82" fill="#ffffff"/>
    <circle cx="86" cy="86" r="76" fill="#1a7f8a"/>
    <path d="M14 70 Q40 20 92 14 Q60 40 58 78 Z" fill="#e9ecec"/>
    <text x="86" y="88" text-anchor="middle" transform="rotate(-12 86 88)" fill="#ffffff" font-family="Source Sans 3, sans-serif" font-weight="600" font-size="19">Special offer for</text>
    <text x="92" y="122" text-anchor="middle" transform="rotate(-12 92 122)" fill="#ffffff" font-family="Source Sans 3, sans-serif" font-weight="700" font-size="38">2011</text>
  </svg>
  <p class="bogof">Buy one<br>Get one free!</p>

  <div class="photo photo-presenter" role="img" aria-label="Photo of a presenter drawing a chart on a whiteboard for colleagues"></div>

  <p class="deal-caption">Buy our Business Foundation SEO package and get an advert on ‘AshbridgeOnline.com for free!</p>
</div>
</body>
</html>
```